Brightmoor Co Trade Show Flyer

We need a brochure design (8.5 x 11) Info in the design (refer to rough draft I drew on Paper): "#1 selling tool to aquire new franchisees has been video testimonials" - Martin L. Greaves, C.E.O Kolva Smoothie Franchise Testimonials - Let your franchisees do the selling for you. Franchisee testimonial: $10,000 / per Franchisee Includes: • 2 minute Video • 1 minute add for your franchise's location • Concept creation • Communication with franchisee • Travel to their location • All rental equipment • 1 round of corrections • Animated logo • Licensed music ******* For 25% Discount section (next to middle box), please put the "Venture Fairground Logo" Great to use on all your social media (USE logos and icons) • Website • YouTube • LinkedIn • Facebook • Instagram • Twitter • Phone calls • Emails • In person meetings Some of our clients: (use the logos I uploaded - in round boxes as in draft) LOGO (Brightmoor Franchise Testimonial) www.brightmoorstories.example (866) 555-0187

Target Market(s)

Franchise owners

Colors

Designer to choose colors to be used in the design.

Requirements

```html
<!DOCTYPE html>
<html lang="en">
<head>
<meta charset="utf-8">
<title>Brightmoor Co – Franchise Testimonials Flyer</title>
<link href="https://fonts.googleapis.com/css2?family=Oswald:wght@600;700&family=Open+Sans:wght@400;700&display=swap" rel="stylesheet">
<style>
  :root {
    --red: #e53d30;
    --black: #000000;
    --dark: #141414;
    --white: #ffffff;
    --teal: #17a58a;
  }
  * { margin: 0; padding: 0; box-sizing: border-box; }
  html, body { width: 927px; height: 1200px; overflow: hidden; background: var(--black); }
  .flyer { position: relative; width: 927px; height: 1200px; overflow: hidden; font-family: "Open Sans", Arial, sans-serif; color: var(--white); }

  .quote-band { position: absolute; top: 0; left: 0; width: 927px; height: 145px; background: var(--black); text-align: center; padding-top: 70px; font-family: "Oswald", "Arial Narrow", sans-serif; font-weight: 600; font-size: 22px; line-height: 30px; letter-spacing: 0.2px; }

  .title-band { position: absolute; top: 145px; left: 0; width: 927px; height: 295px; background: var(--red); text-align: center; font-family: "Oswald", "Arial Narrow", sans-serif; font-weight: 700; font-size: 108px; line-height: 116px; padding-top: 30px; letter-spacing: 1px; }

  .hero-photo { position: absolute; top: 440px; left: 0; width: 927px; height: 515px; background: radial-gradient(ellipse at 75% 70%, #3a3a3a 0%, #202020 40%, #0c0c0c 100%); }

  .tagline { position: absolute; top: 450px; left: 0; width: 927px; text-align: center; font-weight: 700; font-size: 34px; }

  .price-label { position: absolute; top: 516px; left: 88px; width: 445px; height: 57px; background: var(--red); font-weight: 700; font-size: 20px; line-height: 24px; padding: 5px 0 0 22px; }

  .inclusions { position: absolute; top: 574px; left: 86px; list-style: none; font-size: 24px; line-height: 27.2px; }
  .inclusions li { display: flex; align-items: center; }
  .inclusions svg { width: 22px; height: 20px; margin-right: 2px; flex: none; }

  .discount-badge { position: absolute; top: 515px; left: 573px; width: 122px; height: 122px; }
  .discount-text { position: absolute; top: 532px; left: 573px; width: 122px; text-align: center; }
  .discount-text .pct { display: block; font-family: "Oswald", "Arial Narrow", sans-serif; font-weight: 700; font-size: 38px; line-height: 42px; }
  .discount-text .for { display: block; font-weight: 700; font-size: 11px; }
  .partner-badge { position: absolute; top: 538px; left: 698px; width: 81px; height: 50px; background: var(--teal); }

  .trusted-title { position: absolute; top: 834px; left: 110px; color: var(--red); font-weight: 700; font-size: 21px; }
  .clients { position: absolute; top: 862px; left: 91px; display: flex; gap: 16px; }
  .client { width: 84px; height: 84px; border-radius: 50%; background: var(--white); color: var(--dark); display: flex; align-items: center; justify-content: center; text-align: center; font-weight: 700; font-size: 11px; line-height: 13px; padding: 8px; }
  .client:nth-child(2) { margin-left: 0; }

  .footer { position: absolute; top: 955px; left: 0; width: 927px; height: 245px; background: var(--black); }
  .brand { position: absolute; top: 1030px; left: 62px; display: flex; align-items: center; gap: 14px; }
  .brand-dot { width: 46px; height: 46px; border-radius: 50%; background: var(--white); }
  .brand-name { font-weight: 700; font-size: 46px; color: var(--white); letter-spacing: 1px; }

  .socials { position: absolute; top: 988px; left: 545px; display: flex; gap: 22px; }
  .socials span { width: 30px; height: 30px; border-radius: 50%; background: var(--red); }

  .phone { position: absolute; top: 1025px; left: 437px; display: flex; align-items: center; gap: 6px; color: var(--red); font-weight: 700; font-size: 46px; }
  .phone svg { width: 30px; height: 34px; }
  .website { position: absolute; top: 1083px; left: 400px; display: flex; align-items: center; gap: 8px; font-weight: 700; font-size: 30px; }
  .website svg { width: 28px; height: 28px; }
</style>
</head>
<body>
<main class="flyer">
  <header class="quote-band">
    <p>#1 selling tool to aquire new franchisees has been video testimonials"<br>Martin L. Greaves, C.E.O Kolva Smoothie</p>
  </header>

  <h1 class="title-band">FRANCHISE<br>TESTIMONIALS</h1>

  <div class="hero-photo" role="img" aria-label="Dark photo of a film crew with a video camera and monitor recording an interview"></div>

  <p class="tagline">Let your franchisees do the selling for you.</p>

  <p class="price-label">Franchisee testimonial:<br>$10,000 / per Franchisee Includes:</p>

  <ul class="inclusions">
    <li><svg viewBox="0 0 22 20"><path d="M3 11 L8 16 L19 3" fill="none" stroke="#e53d30" stroke-width="4" stroke-linecap="round"/></svg>2 minute Video</li>
    <li><svg viewBox="0 0 22 20"><path d="M3 11 L8 16 L19 3" fill="none" stroke="#e53d30" stroke-width="4" stroke-linecap="round"/></svg>1 minute add for your franchise's location</li>
    <li><svg viewBox="0 0 22 20"><path d="M3 11 L8 16 L19 3" fill="none" stroke="#e53d30" stroke-width="4" stroke-linecap="round"/></svg>Concept creation</li>
    <li><svg viewBox="0 0 22 20"><path d="M3 11 L8 16 L19 3" fill="none" stroke="#e53d30" stroke-width="4" stroke-linecap="round"/></svg>Communication with franchisee</li>
    <li><svg viewBox="0 0 22 20"><path d="M3 11 L8 16 L19 3" fill="none" stroke="#e53d30" stroke-width="4" stroke-linecap="round"/></svg>Travel to their location</li>
    <li><svg viewBox="0 0 22 20"><path d="M3 11 L8 16 L19 3" fill="none" stroke="#e53d30" stroke-width="4" stroke-linecap="round"/></svg>All rental equipment</li>
    <li><svg viewBox="0 0 22 20"><path d="M3 11 L8 16 L19 3" fill="none" stroke="#e53d30" stroke-width="4" stroke-linecap="round"/></svg>1 round of corrections</li>
    <li><svg viewBox="0 0 22 20"><path d="M3 11 L8 16 L19 3" fill="none" stroke="#e53d30" stroke-width="4" stroke-linecap="round"/></svg>Animated logo</li>
    <li><svg viewBox="0 0 22 20"><path d="M3 11 L8 16 L19 3" fill="none" stroke="#e53d30" stroke-width="4" stroke-linecap="round"/></svg>Licensed music</li>
  </ul>

  <svg class="discount-badge" viewBox="0 0 122 122" aria-hidden="true">
    <polygon fill="#e53d30" points="61,2 70,14 84,7 88,22 103,21 101,36 115,42 107,55 119,64 107,73 113,87 99,91 99,106 84,104 78,118 66,110 56,121 47,110 33,116 30,101 15,100 18,86 5,79 14,67 3,57 15,49 10,35 25,32 27,17 41,20 48,7 57,16"/>
  </svg>
  <p class="discount-text"><span class="pct">25%</span><span class="for">DISCOUNT FOR:</span></p>
  <div class="partner-badge" role="img" aria-label="Venture Fairground badge"></div>

  <p class="trusted-title">Trusted by:</p>
  <div class="clients">
    <div class="client">Corvale Creamery</div>
    <div class="client">Dayline Mart</div>
    <div class="client">Kolva Smoothie</div>
    <div class="client">Neatwell Cleaning</div>
  </div>

  <footer class="footer"></footer>
  <div class="brand"><span class="brand-dot"></span><span class="brand-name">Brightmoor</span></div>

  <div class="socials" aria-label="Social channels"><span></span><span></span><span></span><span></span><span></span></div>

  <p class="phone">
    <svg viewBox="0 0 30 34" aria-hidden="true"><path d="M8 3 L13 10 L10 13 Q13 21 19 25 L22 22 L28 27 L24 32 Q12 31 5 18 Q2 10 8 3 Z" fill="#e53d30"/></svg>(866) 555-0187
  </p>
  <p class="website">
    <svg viewBox="0 0 28 28" aria-hidden="true"><g fill="none" stroke="#e53d30" stroke-width="2.4"><circle cx="14" cy="14" r="12"/><ellipse cx="14" cy="14" rx="5" ry="12"/><path d="M2 14 H26 M4 8 H24 M4 20 H24"/></g></svg>brightmoorstories.example
  </p>
</main>
</body>
</html>
```